Brindle Logistics Business Card Design

We are a trucking and warehousing company. We run freight in the US manly from the Pacific NW to TX and back up the the PNW. We also do warehousing where we store, move, and distribute freight. Looking for a clean and modern design of business card. We would like to look rich and elegant. Attached is our logo.

Industry/Entity Type

Trucking Company

Contact Information for Business Card

Looking for a clean and modern design of business card. We would like to look rich and elegant.

Font styles to use
Sans Serif

Colors

Designer to choose colors to be used in the design.

Requirements
Must have
• logo but it should not dominate the card
Should not have
• logo should not dominate the card

```html
<!DOCTYPE html>
<html lang="en">
<head>
<meta charset="utf-8">
<title>Brindle Logistics Business Card</title>
<link href="https://fonts.googleapis.com/css2?family=Lato:wght@400;700;900&display=swap" rel="stylesheet">
<style>
  :root {
    --stage: #1d1e20;
    --brand-blue: #1f7fd0;
    --brand-blue-deep: #1769b5;
    --paper: #ffffff;
    --ink: #3a3b3d;
    --swoop: #3d3e41;
  }
  * { box-sizing: border-box; margin: 0; padding: 0; }
  html, body {
    width: 1200px; height: 900px; overflow: hidden;
    background: var(--stage);
    font-family: "Lato", sans-serif;
  }
  .stage {
    width: 1200px; height: 900px;
    display: flex; flex-direction: column; align-items: center; justify-content: center;
    gap: 36px;
  }
  .card {
    position: relative;
    width: 700px; height: 400px;
    overflow: hidden;
    box-shadow: 0 14px 30px rgba(0,0,0,0.55);
  }

  /* Front */
  .card-front {
    background: linear-gradient(135deg, var(--brand-blue) 0%, var(--brand-blue-deep) 100%);
    color: var(--paper);
  }
  .front-wordmark {
    position: absolute; left: 0; right: 0; top: 150px;
    display: flex; align-items: center; justify-content: center; gap: 16px;
  }
  .front-wordmark .mark-dot {
    width: 20px; height: 20px; border-radius: 50%; background: var(--paper); flex: none;
  }
  .front-wordmark .company-name {
    font-weight: 900; font-size: 38px; letter-spacing: 3px; text-transform: uppercase;
    line-height: 1; white-space: nowrap;
  }
  .front-url {
    position: absolute; left: 0; right: 0; bottom: 70px;
    text-align: center; font-size: 14px; letter-spacing: 5px;
  }

  /* Back */
  .card-back { background: var(--paper); color: var(--ink); }
  .back-shape { position: absolute; inset: 0; }
  .back-wordmark {
    position: absolute; left: 110px; top: 66px;
    display: flex; align-items: center; gap: 14px;
  }
  .back-wordmark .mark-dot {
    width: 18px; height: 18px; border-radius: 50%; background: var(--brand-blue); flex: none;
  }
  .back-wordmark .company-name {
    font-weight: 900; font-size: 30px; letter-spacing: 3px; text-transform: uppercase;
    color: var(--ink); line-height: 1; white-space: nowrap;
  }
  .holder {
    position: absolute; right: 44px; top: 200px; text-align: right; color: var(--paper);
  }
  .holder-name { font-size: 19px; font-weight: 400; }
  .holder-name strong { font-weight: 900; }
  .holder-title { font-size: 14px; margin-top: 3px; }
  .contact-list {
    position: absolute; left: 365px; bottom: 24px;
    list-style: none; color: var(--paper); font-size: 14px;
  }
  .contact-list li { display: flex; align-items: flex-start; gap: 10px; margin-top: 6px; }
  .contact-list .icon { width: 14px; height: 14px; flex: none; margin-top: 2px; }
  .contact-list .address { font-weight: 700; line-height: 1.35; }
</style>
</head>
<body>
<main class="stage">

  <section class="card card-front">
    <div class="front-wordmark">
      <span class="mark-dot"></span>
      <span class="company-name">Brindle Logistics, LLC</span>
    </div>
    <p class="front-url">www.brindlelogistics.com</p>
  </section>

  <section class="card card-back">
    <svg class="back-shape" viewBox="0 0 700 400" width="700" height="400" aria-hidden="true">
      <defs>
        <linearGradient id="bandFill" x1="0" y1="1" x2="1" y2="0">
          <stop offset="0" stop-color="#1f7fd0"/>
          <stop offset="1" stop-color="#1769b5"/>
        </linearGradient>
      </defs>
      <path d="M130 400 Q330 215 700 150 L700 400 Z" fill="url(#bandFill)"/>
      <path d="M95 400 Q300 180 670 128 Q320 200 120 400 Z" fill="#3d3e41"/>
    </svg>

    <div class="back-wordmark">
      <span class="mark-dot"></span>
      <span class="company-name">Brindle Logistics, LLC</span>
    </div>

    <div class="holder">
      <p class="holder-name">Marissa <strong>Holloway</strong></p>
      <p class="holder-title">Chief Executive Officer</p>
    </div>

    <ul class="contact-list">
      <li>
        <svg class="icon" viewBox="0 0 16 16"><path fill="#fff" d="M3.5 1l2.5 3-1.5 2c1 2 3 4 5 5l2-1.5 3 2.5-1.5 2.5C7 14 2 9 1 2.5z"/></svg>
        <span>503 555-0148</span>
      </li>
      <li>
        <svg class="icon" viewBox="0 0 16 16"><path d="M1 3h14v10H1z M2 4l6 5 6-5" fill="none" stroke="#fff" stroke-width="1.6"/></svg>
        <span>marissa@brindlelogistics.com</span>
      </li>
      <li>
        <svg class="icon" viewBox="0 0 16 16"><path fill="#fff" d="M8 1a5 5 0 0 1 5 5c0 4-5 9-5 9S3 10 3 6a5 5 0 0 1 5-5zm0 3a2 2 0 1 0 0 4 2 2 0 0 0 0-4z"/></svg>
        <span class="address">1820 Harbor Ridge Rd<br>Suite 210, Kent, WA 98032</span>
      </li>
    </ul>
  </section>

</main>
</body>
</html>
```